Webdesign für Data Engineers
Very creative approach and clear winner of competition. Looking forward to further cooperation. Matze
Zielgruppe
Wir machen big data Analytics (Auswertung großer und komplexer Unternehmens- und Web-Daten).
Unsere Kunden sind (große) Industrie- & Konsumgüterhersteller (z.B. Weisse Ware-Hersteller, aber auch online-Handelsunternehmen)
Aufgabenstellung
Uns gefallen Webseiten mit großen, ansprechenden Bildern, klarem Schriftbild und schneller Orientierung. z.B. vorniqa.com, quelmaritz.com
Die Farbgebung sollte sich an unserem Firmenlogo orientieren (blau, grau), das wir mit hochladen. Das Logo sollte natürlich auch präsent sein:-). Wichtig noch folgende Daten zum Logo:
Zur Schrift:
Hauptschrift: Titillium (Bold)
Subline + Fließtext: Antonio
Farben:
Hauptfarbe1: C= 100 M= 20 Y= 0 K=0
Hauptfarbe2: C= 40 M=20 Y=0 K=71
Farbe Subline: C=0 M=0 Y=0 K=50
Ausserdem wäre uns für die spätere Beauftragung noch folgendes wichtig:
- Umsetzung als "WordPress" CMS
- Englisch-Deutsch-Umschaltung
- Zusätzliche Mobilansicht

```html
<!DOCTYPE html>
<html lang="de">
<head>
<meta charset="utf-8">
<title>Quantrel Data – Startseite</title>
<link rel="stylesheet" href="https://fonts.googleapis.com/css2?family=Titillium+Web:wght@400;600;700&family=Antonio:wght@400;700&display=swap">
<style>
  :root {
    --brand-blue: #0a93dd;
    --brand-blue-light: #3fb2ee;
    --brand-slate: #3a4656;
    --navy-deep: #070d18;
    --navy: #0d1a30;
    --hero-blue: #1d4f86;
    --subline-grey: #9a9a9a;
    --white: #ffffff;
    --page-bg: #e9ebee;
  }
  * { margin: 0; padding: 0; box-sizing: border-box; }
  html, body {
    width: 1200px; height: 800px; overflow: hidden;
    background: var(--page-bg);
  }
  .site {
    position: relative; width: 1200px; height: 800px; overflow: hidden;
    background: var(--navy-deep);
    font-family: "Antonio", sans-serif;
    color: var(--white);
  }
  .hero-visual {
    position: absolute; inset: 0;
    background:
      radial-gradient(ellipse 420px 330px at 62% 45%, rgba(70,140,210,.55), transparent 70%),
      radial-gradient(ellipse 300px 260px at 40% 60%, rgba(40,110,180,.45), transparent 70%),
      linear-gradient(90deg, var(--navy-deep) 0%, var(--navy) 22%, var(--hero-blue) 55%, var(--navy) 80%, var(--navy-deep) 100%);
  }
  .site-header {
    position: absolute; top: 0; left: 0; right: 0; height: 54px;
    background: rgba(5,9,16,.85);
  }
  .brand {
    position: absolute; left: 255px; top: 16px;
    display: flex; align-items: center; gap: 8px;
  }
  .brand-mark { width: 22px; height: 22px; background: var(--white); }
  .brand-name {
    font-family: "Titillium Web", sans-serif; font-weight: 700;
    font-size: 16px; line-height: 22px; color: var(--white);
  }
  .main-nav {
    position: absolute; left: 530px; top: 21px;
    display: flex; gap: 7px;
    font-family: "Titillium Web", sans-serif; font-weight: 600; font-size: 9px;
  }
  .main-nav a { color: var(--white); text-decoration: none; }
  .main-nav a.is-active { color: var(--brand-blue-light); }
  .main-nav .sep { color: var(--subline-grey); }
  .hero-copy {
    position: absolute; left: 0; right: 0; top: 308px; text-align: center;
  }
  .hero-title {
    font-family: "Titillium Web", sans-serif; font-weight: 700;
    font-size: 41px; letter-spacing: -1px; line-height: 1.1;
  }
  .hero-subline {
    font-size: 13px; letter-spacing: 2px; color: #cfd6df; margin-top: 6px;
  }
  .cta {
    display: inline-block; margin-top: 18px;
    background: var(--brand-blue); color: var(--white);
    font-family: "Titillium Web", sans-serif; font-weight: 700;
    font-size: 10px; letter-spacing: 1.5px; padding: 4px 20px;
  }
  .slider-arrow {
    position: absolute; top: 318px; width: 10px; height: 40px;
    border: 1px solid rgba(255,255,255,.5); background: rgba(0,0,0,.35);
  }
  .slider-arrow.prev { left: 6px; }
  .slider-arrow.next { right: 6px; }
  .lower-wave { position: absolute; left: 0; bottom: 0; width: 1200px; height: 260px; }
  .device-visual { position: absolute; left: 0; bottom: 0; width: 1200px; height: 260px; }
  .social-icons {
    position: absolute; left: 322px; top: 662px; display: flex; gap: 12px;
  }
  .social-icons span { width: 10px; height: 8px; background: rgba(255,255,255,.45); }
</style>
</head>
<body>
<div class="site">
  <div class="hero-visual" role="img" aria-label="Geschäftsmann zeichnet Erfolgsdiagramme und Weltkarte auf eine transparente Datenoberfläche"></div>

  <header class="site-header">
    <div class="brand">
      <span class="brand-mark"></span>
      <span class="brand-name">Quantrel Data</span>
    </div>
    <nav class="main-nav">
      <a class="is-active" href="#">Home</a><span class="sep">•</span>
      <a href="#">Unser Ansatz</a><span class="sep">•</span>
      <a href="#">Unsere Services</a><span class="sep">•</span>
      <a href="#">Unsere Projekte</a><span class="sep">•</span>
      <a href="#">Das Unternehmen</a><span class="sep">•</span>
      <a href="#">Kontakt</a>
    </nav>
  </header>

  <div class="slider-arrow prev"></div>
  <div class="slider-arrow next"></div>

  <section class="hero-copy">
    <h1 class="hero-title">Lorem ipsum dolor sit amet</h1>
    <p class="hero-subline">Lorem ipsum dolor sit amet, consectetur adipiscing elit</p>
    <span class="cta">START TRIAL</span>
  </section>

  <div class="social-icons"><span></span><span></span><span></span><span></span><span></span></div>

  <svg class="lower-wave" viewBox="0 0 1200 260" preserveAspectRatio="none" aria-hidden="true">
    <path d="M0 200 C 300 190, 700 160, 1200 60 L1200 260 L0 260 Z" fill="var(--brand-blue)"/>
    <path d="M0 214 C 320 206, 720 180, 1200 82 L1200 260 L0 260 Z" fill="var(--white)"/>
  </svg>

  <svg class="device-visual" viewBox="0 0 1200 260" role="img" aria-label="Bildschirm mit Dashboard-Ansicht der Datenanalyse">
    <defs>
      <linearGradient id="dashboard-fill" x1="0" y1="0" x2="1" y2="1">
        <stop offset="0" stop-color="#e4eaf1"/>
        <stop offset="1" stop-color="#c7d5e4"/>
      </linearGradient>
    </defs>
    <polygon points="670,260 1107,80 1107,260" fill="#1b1f26"/>
    <polygon points="700,260 1095,96 1095,260" fill="url(#dashboard-fill)"/>
  </svg>
</div>
</body>
</html>
```